Helpdesk Brochure

Would like to revamp an old brochure for a conference
Can I please add our 1300 857 619 in the footer
Printing this on a double sided Brochure

```html
<!DOCTYPE html>
<html lang="en">
<head>
<meta charset="utf-8">
<title>DeskPoint Brochure</title>
<link rel="stylesheet" href="https://fonts.googleapis.com/css2?family=Archivo+Black&family=Montserrat:wght@400;500;600;700&display=swap">
<style>
:root{
  --orange:#f26b21;
  --black:#111111;
  --ink:#1d1d1d;
  --white:#ffffff;
  --stage:#f0eeee;
  --pill-line:#d9d9d9;
}
*{margin:0;padding:0;box-sizing:border-box}
html,body{width:1200px;height:1200px;overflow:hidden;background:var(--stage)}
body{position:relative;font-family:"Montserrat",sans-serif;color:var(--ink)}
.page{position:absolute;top:230px;width:842px;height:1189px;background:var(--white);
  transform:scale(0.6211);transform-origin:0 0;overflow:hidden;box-shadow:0 10px 30px rgba(0,0,0,.18)}
.page--front{left:53px}
.page--back{left:625px}
.shape{position:absolute;left:0;top:0}
.brand{position:absolute;display:flex;align-items:center;gap:12px;white-space:nowrap;
  font-family:"Montserrat",sans-serif;font-weight:700;font-size:42px;color:var(--orange);letter-spacing:1px}
.brand__dot{width:28px;height:28px;border-radius:50%;background:var(--black)}
.brand--small{font-size:28px;gap:9px;letter-spacing:.5px}
.brand--small .brand__dot{width:20px;height:20px}
.headline{position:absolute;left:35px;top:258px;font-family:"Archivo Black",sans-serif;line-height:1;text-transform:uppercase}
.headline .h-small{display:block;font-size:43px;color:var(--black);letter-spacing:.5px}
.headline .h-big{display:block;font-size:70px;color:var(--white);margin-top:8px;line-height:.95}
.headline .h-tag{display:block;font-size:33px;color:var(--black);line-height:1.17;margin-top:6px}
.intro{position:absolute;left:35px;top:600px;width:770px;font-size:19.5px;line-height:27px;text-align:justify;text-align-last:left}
.band{position:absolute;left:0;height:37px;background:var(--black);color:var(--white);
  font-weight:700;font-size:22px;line-height:37px;padding-left:35px;letter-spacing:.3px;
  clip-path:polygon(0 0,100% 0,calc(100% - 16px) 100%,0 100%)}
.service{position:absolute;width:370px}
.pill{display:flex;align-items:center;gap:8px;width:336px;height:38px;border:2px solid var(--pill-line);
  border-radius:19px;padding-left:2px;font-weight:600;font-size:21.5px;color:var(--orange);white-space:nowrap}
.pill svg{flex:none}
.service p{margin-top:4px;font-size:19.5px;line-height:27px;white-space:nowrap}
.touch{position:absolute;left:446px;top:460px;width:396px}
.touch h3{font-size:21px;font-weight:700;color:var(--orange);letter-spacing:.3px;padding-bottom:8px;border-bottom:4px solid var(--orange)}
.touch__row{display:flex;gap:12px;font-size:19.5px;line-height:27px;margin-top:10px}
.touch__row svg{flex:none;margin-top:4px}
.footer{position:absolute;left:0;bottom:0;width:842px;height:84px;background:var(--black);border-top:5px solid var(--orange);
  color:var(--white);font-size:21px}
.footer__phone{position:absolute;left:35px;top:24px;display:flex;align-items:center;gap:10px}
.footer__rule{position:absolute;left:301px;top:18px;width:2px;height:32px;background:var(--white)}
.footer__web{position:absolute;left:413px;top:24px;display:flex;align-items:center;gap:12px}
</style>
</head>
<body>

<!-- Front page -->
<section class="page page--front">
  <div class="brand" style="left:35px;top:92px"><span class="brand__dot"></span>DeskPoint</div>

  <svg class="shape" width="842" height="1189" viewBox="0 0 842 1189" aria-hidden="true">
    <rect x="0" y="245" width="842" height="346" fill="var(--orange)"/>
    <path d="M322 62 L505 555 Q515 578 542 578 L842 578 L842 62 Z" fill="var(--black)"/>
  </svg>
  <svg class="shape" width="842" height="1189" viewBox="0 0 842 1189" role="img" aria-label="Photo of hands typing on a laptop keyboard with glowing security and network icons">
    <defs>
      <linearGradient id="keyboardPhoto" x1="0" y1="0" x2="1" y2="1">
        <stop offset="0" stop-color="#b9a294"/>
        <stop offset=".45" stop-color="#6e5b52"/>
        <stop offset="1" stop-color="#2e2a2b"/>
      </linearGradient>
    </defs>
    <path d="M338 37 L842 37 L842 545 L548 545 Q527 545 519 525 L327 58 Q322 37 338 37 Z" fill="url(#keyboardPhoto)"/>
  </svg>

  <h1 class="headline">
    <span class="h-small">Melbourne’s</span>
    <span class="h-big">Leading<br>IT<br>Support</span>
    <span class="h-tag">Taking care of<br>your IT headaches</span>
  </h1>

  <p class="intro">We partner with all types of businesses to solve their IT problems with continuous ongoing support and solutions that work.</p>

  <div class="band" style="top:669px;width:512px">CLOUD PHONE SYSTEMS &amp; INTERNET</div>

  <div class="service" style="left:35px;top:722px">
    <div class="pill"><svg width="32" height="32" viewBox="0 0 32 32"><circle cx="16" cy="16" r="15" fill="var(--orange)"/><path d="M11 9l3 3-2 2q2 4 6 6l2-2 3 3-2 3q-9-1-12-12z" fill="#fff"/></svg>VoIP &amp; Phone Systems</div>
    <p>We provide expert services in<br>installation and management for<br>office phone lines, VoIP and<br>communications hardware and<br>systems.</p>
  </div>
  <div class="service" style="left:445px;top:722px">
    <div class="pill"><svg width="32" height="32" viewBox="0 0 32 32"><circle cx="16" cy="16" r="15" fill="var(--orange)"/><path d="M9 10h14v10h-9l-4 3v-3h-1z" fill="#fff"/><path d="M12 13h8M12 16h8" stroke="var(--orange)" stroke-width="1.5"/></svg>SMS Gateway</div>
    <p>Unlock seamless communication<br>with our cutting-edge SMS Gateway<br>services, ensuring instant and<br>reliable message delivery for your<br>business needs.</p>
  </div>
  <div class="service" style="left:35px;top:920px">
    <div class="pill"><svg width="32" height="32" viewBox="0 0 32 32"><circle cx="16" cy="16" r="15" fill="var(--orange)"/><circle cx="16" cy="12" r="3.2" fill="#fff"/><circle cx="10" cy="14" r="2.4" fill="#fff"/><circle cx="22" cy="14" r="2.4" fill="#fff"/><path d="M10 23q6-9 12 0z M5 22q5-7 9-2z M27 22q-5-7-9-2z" fill="#fff"/></svg>Team Workspace Calling</div>
    <p>Experience the next level of<br>collaboration with our Team<br>Workspace calling services,<br>empowering your team with<br>seamless communication.</p>
  </div>
  <div class="service" style="left:445px;top:920px">
    <div class="pill"><svg width="32" height="32" viewBox="0 0 32 32"><circle cx="16" cy="16" r="15" fill="var(--orange)"/><path d="M7 13q9-8 18 0M10 16.5q6-5 12 0M13 20q3-2.5 6 0" stroke="#fff" stroke-width="2.2" fill="none" stroke-linecap="round"/><circle cx="16" cy="23" r="1.8" fill="#fff"/></svg>DSL, Fibre &amp; 4G Internet</div>
    <p>Stay connected, delivering reliable<br>and high-speed connectivity tailored<br>to your business requirements.</p>
  </div>

  <footer class="footer">
    <div class="footer__phone"><svg width="24" height="24" viewBox="0 0 24 24"><path d="M5 3l4 4-2 2.5q2.5 5 7.5 7.5L17 15l4 4-3 3Q6 20 2 6z" fill="none" stroke="var(--orange)" stroke-width="2"/></svg>1300 857 619</div>
    <div class="footer__rule"></div>
    <div class="footer__web"><svg width="24" height="24" viewBox="0 0 24 24" fill="none" stroke="var(--orange)" stroke-width="1.8"><circle cx="12" cy="12" r="10"/><ellipse cx="12" cy="12" rx="4.5" ry="10"/><path d="M2 12h20M4 7h16M4 17h16"/></svg>www.deskpointit.com.au</div>
  </footer>
</section>

<!-- Back page -->
<section class="page page--back">
  <div class="band" style="top:38px;width:356px">MANAGED I.T SERVICES</div>

  <div class="service" style="left:35px;top:93px">
    <div class="pill"><svg width="32" height="32" viewBox="0 0 32 32"><circle cx="16" cy="16" r="15" fill="var(--orange)"/><rect x="8" y="9" width="16" height="11" rx="1" fill="#fff"/><path d="M13 24h6M16 20v4" stroke="#fff" stroke-width="2"/></svg>Managed I.T Support</div>
    <p>Optimize your business operations,<br>providing proactive solutions and<br>assistance to ensure smooth and<br>efficient technology management.</p>
  </div>
  <div class="service" style="left:446px;top:93px;width:396px">
    <div class="pill"><svg width="32" height="32" viewBox="0 0 32 32"><circle cx="16" cy="16" r="15" fill="var(--orange)"/><path d="M16 7l8 3v6q0 6-8 9-8-3-8-9v-6z" fill="none" stroke="#fff" stroke-width="2"/><rect x="13" y="14" width="6" height="5" fill="#fff"/></svg>Cybersecurity Solutions</div>
    <p>Protect your digital assets and<br>safeguard your business,<br>withdefense mechanisms an<br>proactive monitoring to mitigate<br>cyber threats effectively.</p>
  </div>
  <div class="service" style="left:35px;top:288px">
    <div class="pill"><svg width="32" height="32" viewBox="0 0 32 32"><circle cx="16" cy="16" r="15" fill="var(--orange)"/><path d="M10 20a4 4 0 010-8 6 6 0 0111 0 4 4 0 011 8z" fill="#fff"/><path d="M16 20v5M12 25h8" stroke="#fff" stroke-width="2"/></svg>Cloud Servers &amp; Backups</div>
    <p>Secure your data, ensuring reliable<br>storage, seamless accessibility, and<br>robust disaster recovery capabilities<br>for your business.</p>
  </div>
  <div class="service" style="left:446px;top:288px;width:396px">
    <div class="pill"><svg width="32" height="32" viewBox="0 0 32 32"><circle cx="16" cy="16" r="15" fill="var(--orange)"/><rect x="8" y="10" width="16" height="12" rx="1" fill="none" stroke="#fff" stroke-width="2"/><path d="M8 11l8 6 8-6" fill="none" stroke="#fff" stroke-width="2"/></svg>Cloud Office Email Packs</div>
    <p>Elevate your email communication,<br>providing advanced features,<br>security enhancements, and<br>seamless integration.</p>
  </div>
  <div class="service" style="left:35px;top:460px">
    <div class="pill"><svg width="32" height="32" viewBox="0 0 32 32" fill="none"><circle cx="16" cy="16" r="15" fill="var(--orange)"/><g stroke="#fff" stroke-width="1.6"><circle cx="16" cy="16" r="9"/><ellipse cx="16" cy="16" rx="4" ry="9"/><path d="M7 16h18M9 11h14M9 21h14"/></g></svg>Domains &amp; Websites</div>
    <p>Establish your online presence with<br>ease, offering personalised domain<br>registration, expert website design,<br>and reliable hosting solutions for<br>your business.</p>
  </div>

  <div class="touch">
    <h3>GET IN TOUCH</h3>
    <div class="touch__row"><svg width="20" height="18" viewBox="0 0 20 18" fill="none" stroke="var(--orange)" stroke-width="1.8"><rect x="1" y="2" width="18" height="14"/><path d="M1 3l9 7 9-7M1 16l7-6M19 16l-7-6"/></svg>sales@deskpointit.com.au</div>
    <div class="touch__row"><svg width="20" height="22" viewBox="0 0 20 22" fill="none" stroke="var(--orange)" stroke-width="1.8"><path d="M10 15q-6-6-6-9a6 6 0 0112 0q0 3-6 9z"/><circle cx="10" cy="6" r="2"/><path d="M3 18h14"/></svg><span>B3/18 Carrick Lane,<br>Tullamarine VIC 3043</span></div>
  </div>

  <svg class="shape" width="842" height="1189" viewBox="0 0 842 1189" aria-hidden="true">
    <path d="M345 624 L842 624 L842 1099 L170 1099 Q155 1099 161 1080 L300 650 Q310 624 345 624 Z" fill="var(--orange)"/>
  </svg>
  <svg class="shape" width="842" height="1189" viewBox="0 0 842 1189" role="img" aria-label="Photo of a hand touching a tablet with glowing cloud and network icons">
    <defs>
      <radialGradient id="tabletPhoto" cx=".55" cy=".35" r=".8">
        <stop offset="0" stop-color="#ffd27a"/>
        <stop offset=".35" stop-color="#f08a2a"/>
        <stop offset=".75" stop-color="#a3481b"/>
        <stop offset="1" stop-color="#3b2a1c"/>
      </radialGradient>
    </defs>
    <path d="M362 659 L842 659 L842 1099 L192 1099 Q166 1099 173 1077 L330 677 Q337 659 362 659 Z" fill="url(#tabletPhoto)"/>
  </svg>

  <div class="brand brand--small" style="left:40px;top:780px"><span class="brand__dot"></span>DeskPoint</div>

  <footer class="footer">
    <div class="footer__phone"><svg width="24" height="24" viewBox="0 0 24 24"><path d="M5 3l4 4-2 2.5q2.5 5 7.5 7.5L17 15l4 4-3 3Q6 20 2 6z" fill="none" stroke="var(--orange)" stroke-width="2"/></svg>1300 857 619</div>
    <div class="footer__rule"></div>
    <div class="footer__web"><svg width="24" height="24" viewBox="0 0 24 24" fill="none" stroke="var(--orange)" stroke-width="1.8"><circle cx="12" cy="12" r="10"/><ellipse cx="12" cy="12" rx="4.5" ry="10"/><path d="M2 12h20M4 7h16M4 17h16"/></svg>www.deskpointit.com.au</div>
  </footer>
</section>

</body>
</html>
```